institute for female grief councelors needs a design for its facebook group

Each year about 350.000 German women do have a misscarriage while they are pregnant. Their pain and grief is soul deep. Lots of them are stay still in grief even if they have got other children who are healthy and alive. Lots of these women have got difficulty in finally letting go pain, rage and grief. Some are even still in grief after more than twenty or thirty years of having lost their child through misscarriage!!!!

With this facebook group I want to give hope, trust and support as well as helpful advice in coping with this deep soul pain after having lost your child through misscarriage.

The facebook cover shall cause a great curiosity and fascination to the mothers so that they are interested in joining our facebook group.

At our institute women can book a-one-year-training to become a certified "Coach for WolkenHerzen" (grief councelor for women who are in deep grief after their misscarriage).

In Germany children who died through misscarriage are named "Sternenkind" (STARCHILD).
Therefore I want to have at least one shing star at the facebook cover symbolizing the still shining soullight of the dead child watching its mother who is still living on earth.

On the left side of the uploaded file you see the planet venus: symbol for mothers / female side of life.
The red sky colour symbolizes the colour of the uterus, the embryo's home before having died through misscarriage.
It ist also possible to include the silhoutte of a mother / several mothers looking up into the red / blue sky to watch the shining soullight of their dead child.

The facebook cover MUST include the following sentence:

Mama, ich lasse mein Licht für dich leuchten

(Mummy, I let my soullight shine for you)

Target Market(s)

German speaking mothers

Industry/Entity Type

coaching

Font styles to use
Script

Colors

Designer to choose colors to be used in the design.

Requirements
Must have
• golden fond writing, at least one shing star, silhouette of one / several mothers (no model typa - normal woman)
Nice to have
• planet venus - red background cover (like uterus colour)
Should not have
• mothers who like like a model or filmstar

```html
<!DOCTYPE html>
<html lang="de">
<head>
<meta charset="utf-8">
<title>Sternenkind – Mama, ich lasse mein Licht für dich leuchten</title>
<link rel="stylesheet" href="https://fonts.googleapis.com/css2?family=Great+Vibes&display=swap">
<style>
  :root {
    --night-deep: #07061a;
    --night-blue: #151338;
    --night-violet: #2a1638;
    --uterus-red: #5a1a22;
    --glow-red: #c8321e;
    --star-core: #fffbe8;
    --star-halo: #ff7a3a;
    --venus-light: #e6d2a2;
    --venus-mid: #c9a96a;
    --venus-dark: #8a6a3a;
    --gold-light: #f6d77a;
    --gold-mid: #d9a527;
    --gold-deep: #a86f12;
  }
  * { margin: 0; padding: 0; box-sizing: border-box; }
  html, body {
    width: 1200px;
    height: 527px;
    overflow: hidden;
    background: var(--night-deep);
  }
  .cover {
    position: relative;
    width: 1200px;
    height: 527px;
    overflow: hidden;
  }
  .night-sky {
    position: absolute;
    inset: 0;
    background:
      radial-gradient(ellipse 520px 360px at 980px 60px, rgba(200, 50, 30, 0.55), transparent 70%),
      radial-gradient(ellipse 700px 500px at 1200px 0px, var(--uterus-red), transparent 75%),
      linear-gradient(110deg, var(--night-blue) 0%, var(--night-deep) 45%, var(--night-violet) 100%);
  }
  .shining-star {
    position: absolute;
    left: 966px;
    top: 80px;
    width: 0;
    height: 0;
  }
  .shining-star svg {
    position: absolute;
    left: -130px;
    top: -130px;
  }
  .venus {
    position: absolute;
    left: -7px;
    top: 22px;
    width: 526px;
    height: 526px;
    border-radius: 50%;
    background:
      radial-gradient(circle at 42% 38%, var(--venus-light) 0%, var(--venus-mid) 55%, var(--venus-dark) 100%);
    box-shadow: 0 0 40px rgba(230, 200, 140, 0.18);
  }
  .message {
    position: absolute;
    inset: 0;
    font-family: "Great Vibes", cursive;
    font-weight: 400;
    line-height: 1;
  }
  .message span {
    position: absolute;
    white-space: nowrap;
    background: linear-gradient(180deg, var(--gold-light) 0%, var(--gold-mid) 55%, var(--gold-deep) 100%);
    -webkit-background-clip: text;
    background-clip: text;
    color: transparent;
    filter: drop-shadow(0 2px 3px rgba(0, 0, 0, 0.6));
  }
  .message .greeting { left: 612px; top: 128px; font-size: 96px; }
  .message .line-one { left: 580px; top: 242px; font-size: 66px; }
  .message .line-two { left: 600px; top: 316px; font-size: 66px; }
</style>
</head>
<body>
  <main class="cover">
    <div class="night-sky" role="img" aria-label="Dunkler Sternenhimmel, nach rechts oben in warmes Rot übergehend"></div>

    <div class="shining-star" aria-hidden="true">
      <svg width="260" height="260" viewBox="0 0 260 260">
        <defs>
          <radialGradient id="star-glow" cx="50%" cy="50%" r="50%">
            <stop offset="0%" stop-color="var(--star-core)"/>
            <stop offset="12%" stop-color="var(--star-core)"/>
            <stop offset="30%" stop-color="var(--star-halo)" stop-opacity="0.8"/>
            <stop offset="60%" stop-color="var(--glow-red)" stop-opacity="0.3"/>
            <stop offset="100%" stop-color="var(--glow-red)" stop-opacity="0"/>
          </radialGradient>
        </defs>
        <circle cx="130" cy="130" r="130" fill="url(#star-glow)"/>
        <path d="M130 40 L134 126 L220 130 L134 134 L130 220 L126 134 L40 130 L126 126 Z" fill="var(--star-core)" opacity="0.85"/>
        <circle cx="130" cy="130" r="12" fill="#ffffff"/>
      </svg>
    </div>

    <div class="venus" role="img" aria-label="Planet Venus, davor die Silhouette einer Mutter, die betend zum Himmel aufblickt"></div>

    <h1 class="message">
      <span class="greeting">Mama,</span>
      <span class="line-one">ich lasse mein Licht</span>
      <span class="line-two">für dich leuchten</span>
    </h1>
  </main>
</body>
</html>
```